Website for an electrical contractor :)

We are after a web site which can show pictures of our jobs and our capability in a professional, creative and easily understood way.

----- Brightmoor Electrical ------

We really want a visually good looking website with three sections

Section one:
'Completed projects'
We have a few pictures of jobs which we've completed and would like to show off with a brief description. (see uploads)

Section two:
'Our capabilities'
Just a list of what services we offer

Section three:
We would like a 'contact us' section which people can send us a short msg and upload a file for plans to be able to send to us. We would need their name, phone number and email details. We would also need a short privacy policy saying 'we do not disclose information to third parties'.
We also want to display our contact number and postal address

Good luck :)

Target Market(s)

Adults 25 years+
Business owners
Builders
Real estate agents

Industry/Entity Type

Electrical

Colors

Designer to choose colors to be used in the design.

Requirements
Must have
• Visually appealing
Easy to understand
In the 'Completed projects' section, must have a list for each project we do i can upload pictures for it.

```html
<!DOCTYPE html>
<html lang="en">
<head>
<meta charset="UTF-8">
<title>Brightmoor Electrical — Recent Projects</title>
<link rel="stylesheet" href="https://fonts.googleapis.com/css2?family=Open+Sans:wght@300;400&family=Roboto+Condensed:wght@400;700&display=swap">
<style>
  :root {
    --red: #e0161e;
    --ink: #3b3b3b;
    --ink-dark: #111111;
    --band: #edeaea;
    --divider: #4a4a4a;
    --white: #ffffff;
  }
  * { margin: 0; padding: 0; box-sizing: border-box; }
  html, body {
    width: 1200px;
    height: 745px;
    overflow: hidden;
    background: var(--white);
  }
  .page {
    position: relative;
    width: 1200px;
    height: 745px;
    overflow: hidden;
  }

  /* Featured project band */
  .featured {
    position: absolute;
    left: 0; top: 0;
    width: 1200px;
    height: 414px;
    background: var(--band);
    border-top: 3px solid #e2e0e0;
    box-shadow: 0 3px 3px rgba(0,0,0,0.06);
  }
  .featured__heading {
    position: absolute;
    left: 186px;
    top: 80px;
    font-family: "Open Sans", sans-serif;
    font-weight: 300;
    font-size: 53px;
    line-height: 56px;
    color: var(--ink);
    letter-spacing: -0.5px;
  }
  .featured__heading .accent { color: var(--red); font-weight: 400; }
  .featured__divider {
    position: absolute;
    left: 460px;
    top: 12px;
    width: 2px;
    height: 390px;
    background: var(--divider);
  }
  .featured__title {
    position: absolute;
    left: 493px;
    top: 9px;
    font-family: "Open Sans", sans-serif;
    font-weight: 300;
    font-size: 27px;
    color: var(--red);
  }
  .featured__photo {
    position: absolute;
    left: 494px;
    top: 50px;
    width: 487px;
    height: 240px;
    background: linear-gradient(180deg, #4a4742 0%, #9a948a 35%, #bcb6aa 60%, #5b544c 100%);
  }
  .featured__text {
    position: absolute;
    left: 494px;
    top: 297px;
    width: 492px;
    font-family: "Roboto Condensed", sans-serif;
    font-size: 14.5px;
    line-height: 23px;
    color: var(--ink);
  }
  .button {
    position: absolute;
    left: 494px;
    top: 347px;
    width: 119px;
    height: 39px;
    border: 2px solid var(--red);
    border-radius: 5px;
    font-family: "Roboto Condensed", sans-serif;
    font-size: 17px;
    line-height: 35px;
    text-align: center;
    color: var(--red);
    text-decoration: none;
  }

  /* Project cards */
  .project-list {
    position: absolute;
    left: 197px;
    top: 450px;
    display: flex;
    gap: 18px;
  }
  .project-card { width: 257px; }
  .project-card__photo { width: 257px; height: 211px; }
  .project-card__photo--panel { background: linear-gradient(160deg, #6b5f57 0%, #c5402f 45%, #8a7a6a 100%); }
  .project-card__photo--slab { background: linear-gradient(170deg, #7a6f66 0%, #4e4039 50%, #6f6259 100%); }
  .project-card__photo--office { background: linear-gradient(180deg, #3a3733 0%, #6a655e 50%, #8d8f92 75%, #5a5550 100%); }
  .project-card__title {
    margin-top: 10px;
    font-family: "Roboto Condensed", sans-serif;
    font-weight: 700;
    font-size: 17px;
    color: var(--ink-dark);
  }
  .project-card__text {
    margin-top: 4px;
    font-family: "Roboto Condensed", sans-serif;
    font-size: 12.5px;
    color: #222;
  }
  .project-card__link {
    display: inline-block;
    margin-top: 5px;
    font-family: "Roboto Condensed", sans-serif;
    font-size: 12.5px;
    color: var(--red);
    text-decoration: underline;
  }
</style>
</head>
<body>
<main class="page">
  <section class="featured">
    <h1 class="featured__heading">Some of<br>our recent<br><span class="accent">Projects</span></h1>
    <div class="featured__divider"></div>
    <h2 class="featured__title">Project Name</h2>
    <div class="featured__photo" role="img" aria-label="Photo of a finished function room with lounge seating and a curved floor"></div>
    <p class="featured__text">Lorem ipsum dolor sit amet, consectetur adipiscing elit. MLorem ipsum dolor sit amet, consect-etur adipiscing elit. Morbi sagittis varius odio vel interdum.</p>
    <a class="button" href="#">Read more</a>
  </section>

  <section class="project-list">
    <article class="project-card">
      <div class="project-card__photo project-card__photo--panel" role="img" aria-label="Photo of a wired switchboard with red breakers"></div>
      <h3 class="project-card__title">Lorem Ipsum Dolozr Sit Amet</h3>
      <p class="project-card__text">adipiscing elit. MLorem ipsum dolor sit amet,</p>
      <a class="project-card__link" href="#">Read more...</a>
    </article>
    <article class="project-card">
      <div class="project-card__photo project-card__photo--slab" role="img" aria-label="Photo of conduit laid through slab reinforcement"></div>
      <h3 class="project-card__title">Lorem Ipsum Dolor Sit Amet</h3>
      <p class="project-card__text">adipiscing elit. MLorem ipsum dolor sit amet,</p>
      <a class="project-card__link" href="#">Read more...</a>
    </article>
    <article class="project-card">
      <div class="project-card__photo project-card__photo--office" role="img" aria-label="Photo of an office fit-out with ceiling lights and city windows"></div>
      <h3 class="project-card__title">Lorem Ipsum Dolor Sit Amet</h3>
      <p class="project-card__text">adipiscing elit. MLorem ipsum dolor sit amet,</p>
      <a class="project-card__link" href="#">Read more...</a>
    </article>
  </section>
</main>
</body>
</html>
```